Business Card Design

Business sales of reconditioned / used batteries with mobile delivery and install services. Customers base majority are auto car sales lots and individuals.

Card need to convey quality product reliability and quick prompt professional service.

Card must reflect excellence in customer care and product being offered

Target Market(s)

Auto car lots new and used. Auto repair shops. Individuals.

Industry/Entity Type

Business

Contact Information for Business Card

Batteries Q-Volt
Cars, Trucks, Boats, Motorcycles, lawn mowers, power tools
Delivery & install available most vehicles
Mon-Sat 9-6pm
Dale Morrick 501-738-2056
*product warranty 6 month shelf life battery/1 year blems battery

```html
<!DOCTYPE html>
<html lang="en">
<head>
<meta charset="utf-8">
<title>Batteries Q-Volt – Business Card</title>
<link href="https://fonts.googleapis.com/css2?family=Lato:wght@300;400;700;900&display=swap" rel="stylesheet">
<style>
  :root {
    --backdrop: #6a6a6a;
    --card-black: #050505;
    --brand-teal: #1f97b8;
    --accent-orange: #e2742a;
    --rule-orange: #c2561a;
    --name-light: #c9c9c9;
    --name-bold: #e8e8e8;
    --band-blue: #1d4a8a;
    --band-edge: #f2f2f2;
    --white: #ffffff;
  }
  html, body {
    margin: 0;
    padding: 0;
    width: 1200px;
    height: 900px;
    overflow: hidden;
    background: var(--backdrop);
    font-family: "Lato", Arial, sans-serif;
  }
  .business-card {
    position: absolute;
    left: 75px;
    top: 150px;
    width: 1050px;
    height: 600px;
    background: var(--card-black);
    overflow: hidden;
    box-shadow: 0 18px 40px rgba(0,0,0,0.35);
  }
  .card-content {
    position: relative;
    z-index: 2;
    text-align: center;
    padding-top: 88px;
  }
  .company-name {
    margin: 0;
    font-size: 58px;
    font-weight: 700;
    color: var(--brand-teal);
    letter-spacing: -0.5px;
  }
  .services {
    margin: 16px auto 0;
    display: inline-block;
    color: var(--accent-orange);
    font-size: 27px;
    line-height: 1.55;
  }
  .services-line {
    display: block;
    border-bottom: 2px solid var(--rule-orange);
    padding: 0 4px;
  }
  .services-line + .services-line {
    display: inline-block;
  }
  .hours { font-weight: 700; }
  .contact-name {
    margin: 40px 0 0;
    font-size: 40px;
    letter-spacing: 1px;
    text-transform: uppercase;
  }
  .contact-name .first { font-weight: 300; color: var(--name-light); }
  .contact-name .last { font-weight: 700; color: var(--name-bold); }
  .contact-phone {
    margin: 10px 0 0;
    font-size: 27px;
    color: var(--brand-teal);
  }
  .contact-phone .label { font-weight: 900; }
  .warranty-band {
    position: absolute;
    left: 0;
    top: 0;
    z-index: 1;
  }
  .warranty {
    position: absolute;
    z-index: 2;
    left: 0;
    right: 0;
    top: 478px;
    text-align: center;
    color: var(--white);
  }
  .warranty-title {
    margin: 0;
    font-size: 33px;
    font-weight: 700;
    letter-spacing: 0.5px;
  }
  .warranty-terms {
    margin: 10px 0 0;
    font-size: 24px;
    font-weight: 400;
    letter-spacing: 1px;
  }
</style>
</head>
<body>
  <div class="business-card">
    <svg class="warranty-band" width="1050" height="600" viewBox="0 0 1050 600" aria-hidden="true">
      <path d="M0,478 Q525,340 1050,458 L1050,600 L0,600 Z" fill="var(--band-edge)"/>
      <path d="M0,486 Q525,350 1050,466 L1050,600 L0,600 Z" fill="var(--band-blue)"/>
    </svg>

    <div class="card-content">
      <h1 class="company-name">Batteries Q-Volt Cars</h1>
      <div class="services">
        <span class="services-line">Trucks, Boats, Motorcycles, lawn mowers, power tools Delivery</span>
        <span class="services-line">&amp; install available most vehicles <span class="hours">Mon-Sat 9-6pm</span></span>
      </div>
      <p class="contact-name"><span class="first">Dale</span> <span class="last">Morrick</span></p>
      <p class="contact-phone"><span class="label">PHONE:</span> 501-738-2056</p>
    </div>

    <div class="warranty">
      <p class="warranty-title">PRODUCT WARRANTY</p>
      <p class="warranty-terms">6 MONTH SHELF LIFE BATTERY/1 YEAR BLEMS BATTERY</p>
    </div>
  </div>
</body>
</html>
```